New Word Template Design Project

I want design about template plant date palm tree
The size is A4/Users/mibu/Desktop/DSC07540.JPG
/Users/mibu/Desktop/DSC07514.JPG

```html
<!DOCTYPE html>
<html lang="en">
<head>
<meta charset="utf-8">
<title>Business Proposal – Date Palm Nursery</title>
<link href="https://fonts.googleapis.com/css2?family=Roboto:wght@400&family=Source+Sans+3:wght@400;600&display=swap" rel="stylesheet">
<style>
  :root {
    --green: #80bf3b;
    --green-dark: #6fae2d;
    --ink: #1e1e1e;
    --text: #555555;
    --muted: #6d6d6d;
    --cell-grey: #f0f0f0;
    --rule: #cfcfcf;
    --paper: #ffffff;
    --backdrop: #e9e9e7;
  }
  * { box-sizing: border-box; margin: 0; padding: 0; }
  html, body { width: 1200px; height: 854px; overflow: hidden; }
  body { background: var(--backdrop); font-family: "Source Sans 3", Arial, sans-serif; position: relative; }

  .sheet {
    position: absolute; left: 302px; top: 6px;
    width: 596px; height: 842px;
    background: var(--paper);
    box-shadow: 0 2px 10px rgba(0,0,0,.12);
  }
  .hero {
    position: absolute; left: 0; top: 0; width: 596px; height: 236px;
    background: linear-gradient(180deg, #5f8f45 0%, #3f6b30 45%, #2b3a26 75%, #1b1d1b 100%);
    clip-path: polygon(0 0,100% 0,100% 94%,97% 100%,93% 92%,88% 99%,83% 91%,78% 98%,72% 90%,66% 97%,60% 91%,54% 99%,48% 92%,42% 98%,36% 90%,30% 97%,24% 91%,18% 99%,12% 92%,6% 98%,0 93%);
  }
  .title {
    position: absolute; left: 39px; top: 240px;
    font-family: "Roboto", Arial, sans-serif; font-weight: 400;
    font-size: 21px; color: var(--green);
  }
  .intro {
    position: absolute; left: 39px; top: 273px; width: 518px;
    font-size: 11px; line-height: 15px; color: var(--text); text-align: justify;
  }
  .quote {
    position: absolute; left: 39px; top: 344px; width: 518px;
    border-collapse: collapse; font-size: 11px;
  }
  .quote th {
    background: var(--green); color: #fff; font-weight: 400;
    height: 41px; text-align: center;
  }
  .quote th:first-child { border-top-left-radius: 5px; text-align: left; padding-left: 13px; }
  .quote th:last-child { border-top-right-radius: 5px; }
  .quote td {
    height: 39px; text-align: center; color: var(--muted);
    border-bottom: 1px solid var(--rule);
  }
  .quote tr:last-child td { border-bottom: none; }
  .quote .date { background: var(--cell-grey); color: var(--ink); text-align: left; padding-left: 11px; width: 78px; }
  .quote .item { width: 182px; }
  .quote .price { background: var(--cell-grey); color: var(--ink); width: 99px; }
  .quote .qty { width: 59px; }
  .quote .total { background: var(--cell-grey); color: var(--ink); width: 100px; }
  .grand-total {
    position: absolute; left: 457px; top: 627px; width: 101px; height: 34px;
    background: var(--green); color: #fff; font-size: 14px;
    display: flex; align-items: center; justify-content: center;
    border-radius: 0 0 3px 3px;
  }
  .terms-title {
    position: absolute; left: 40px; top: 680px;
    font-size: 13px; color: var(--ink); font-weight: 600;
  }
  .terms {
    position: absolute; left: 39px; top: 704px; width: 518px;
    font-size: 7.2px; line-height: 11px; color: var(--text); text-align: justify;
  }
  .footer-rule { position: absolute; left: 0; top: 767px; width: 596px; height: 3px; background: var(--green); }
  .footer {
    position: absolute; left: 0; top: 773px; width: 596px; height: 69px;
    background: var(--green); color: #fff; font-size: 13px;
    display: flex; align-items: center; justify-content: space-between; padding: 0 41px 0 39px;
  }
  .contact { display: flex; align-items: center; gap: 5px; }
  .contact svg { width: 12px; height: 12px; }
</style>
</head>
<body>
  <div class="sheet">
    <div class="hero" role="img" aria-label="Photograph of young date palm seedlings growing in black nursery bags"></div>

    <h1 class="title">Business Proposals</h1>
    <p class="intro">Lorem ipsum dolor sit amet, consectetur adipiscing elit. Etiam sit amet nisi sit amet nibh dignis sim elementum id suscipit leo. Sed ut condimentum diam. Sed ac nulla libero. Morbi ante ante inte rdum luctus dictum ut, sollicitudin in mi. Donec aliquet lectus quis enim tempor ullamcorper pelle ntesque et neque posuere, gravida lacus molestie, pretium ex. Vivamus in justo ac ante lacinia pharetra.</p>

    <table class="quote">
      <thead>
        <tr><th>Plant Date</th><th>Item Description</th><th>Price</th><th>Qty.</th><th>Total</th></tr>
      </thead>
      <tbody>
        <tr><td class="date">09.10.2020</td><td class="item">Lorem ipsum dolor sit</td><td class="price">$50</td><td class="qty">1</td><td class="total">$50</td></tr>
        <tr><td class="date">09.10.2020</td><td class="item">Lorem ipsum dolor sit</td><td class="price">$150</td><td class="qty">2</td><td class="total">$300</td></tr>
        <tr><td class="date">09.10.2020</td><td class="item">Lorem ipsum dolor sit</td><td class="price">$250</td><td class="qty">1</td><td class="total">$250</td></tr>
        <tr><td class="date">09.10.2020</td><td class="item">Lorem ipsum dolor sit</td><td class="price">$300</td><td class="qty">1</td><td class="total">$300</td></tr>
        <tr><td class="date">09.10.2020</td><td class="item">Lorem ipsum dolor sit</td><td class="price">$350</td><td class="qty">1</td><td class="total">$350</td></tr>
        <tr><td class="date">09.10.2020</td><td class="item">Lorem ipsum dolor sit</td><td class="price">$400</td><td class="qty">1</td><td class="total">$400</td></tr>
      </tbody>
    </table>
    <div class="grand-total">$1650</div>

    <h2 class="terms-title">Terms &amp; Conditions</h2>
    <p class="terms">Lorem ipsum dolor sit amet, consectetur adipiscing elit. Etiam sit amet nisi sit amet nibh dignis sim elementum id suscipit leo. Sed ut condimentum diam. Sed ac nulla libero. Morbi ante ante inte rdum luctus dictum ut, sollicitudin in mi. Donec aliquet lectus quis enim tempor ullamcorper pelle ntesque et neque posuere, gravida lacus molestie, pretium ex. Vivamus in justo ac ante lacinia pharetra.</p>

    <div class="footer-rule"></div>
    <footer class="footer">
      <span class="contact">
        <svg viewBox="0 0 12 12"><circle cx="6" cy="6" r="5.4" fill="none" stroke="#fff" stroke-width="1.1"/><rect x="3" y="4" width="6" height="4" fill="none" stroke="#fff" stroke-width=".9"/><path d="M3 4l3 2.2L9 4" fill="none" stroke="#fff" stroke-width=".9"/></svg>
        info@greenfrondnursery.com
      </span>
      <span class="contact">
        <svg viewBox="0 0 12 12"><circle cx="6" cy="6" r="5.4" fill="none" stroke="#fff" stroke-width="1.1"/><path d="M4 3.3l1.1 1.5-.6.8c.4.9 1 1.5 1.9 1.9l.8-.6 1.5 1.1-.6 1c-2.4-.3-4.3-2.2-4.6-4.6z" fill="#fff"/></svg>
        0145 672 310
      </span>
      <span class="contact">
        <svg viewBox="0 0 12 12"><circle cx="6" cy="6" r="5.4" fill="none" stroke="#fff" stroke-width="1.1"/><circle cx="6" cy="6" r="3" fill="none" stroke="#fff" stroke-width=".9"/><path d="M3 6h6M6 3c-1.3 1.6-1.3 4.4 0 6M6 3c1.3 1.6 1.3 4.4 0 6" fill="none" stroke="#fff" stroke-width=".7"/></svg>
        www.greenfrondnursery.com
      </span>
    </footer>
  </div>
</body>
</html>
```